80s Dance Party invitation/flyer

Im looking for a flyer for an 80’s theme party called Neon Rewind 80’s Dance Party. Date is Saturday, June 26, 2021. Location: Brackenford Village. Uploaded are some sample ideas i like.

```html
<!DOCTYPE html>
<html lang="en">
<head>
<meta charset="utf-8">
<title>Neon Rewind 80’s Dance Party</title>
<link rel="stylesheet" href="https://fonts.googleapis.com/css2?family=Abril+Fatface&family=Bungee&family=Rubik+Dirt&family=Open+Sans:wght@600&display=swap">
<style>
  :root {
    --coral: #ff6a4d;
    --night: #23095a;
    --paper: #ffffff;
    --rose: #d8395f;
    --amber: #f6a623;
    --gold: #f0a11d;
    --leaf: #1d8a3e;
    --forest: #1a6e35;
    --ink: #1c1c1c;
  }
  * { margin: 0; padding: 0; box-sizing: border-box; }
  html, body { width: 848px; height: 1200px; overflow: hidden; background: var(--night); }
  .flyer { position: relative; width: 848px; height: 1200px; overflow: hidden; }
  .backdrop, .lettering { position: absolute; left: 0; top: 0; }
  .headline {
    position: absolute; left: 300px; width: 460px; text-align: center;
    font-family: "Abril Fatface", serif; color: var(--paper);
    letter-spacing: 4px; line-height: 1;
  }
  .headline--top { top: 28px; font-size: 100px; }
  .headline--bottom { top: 150px; font-size: 104px; }
  .art { position: absolute; }
  .art--notes-top { left: 5px; top: 66px; width: 315px; height: 207px; border-radius: 40px;
    background: linear-gradient(160deg, rgba(40,20,20,.55), rgba(244,190,40,.45)); }
  .art--boombox { left: 0; top: 720px; width: 226px; height: 236px; border-radius: 14px;
    background: linear-gradient(180deg, #f0c21e 0 14%, #3fc3cf 14% 60%, #ee2f8a 60%); }
  .art--notes-bottom { left: 334px; top: 942px; width: 326px; height: 160px; border-radius: 60px;
    background: linear-gradient(170deg, rgba(236,180,236,.45), rgba(215,50,110,.45)); }
  .event-date {
    position: absolute; left: 14px; top: 1036px; font-family: "Rubik Dirt", sans-serif;
    font-size: 48px; line-height: 54px; color: var(--forest);
  }
  .event-date span { display: block; }
  .event-date .date-day { padding-left: 24px; color: var(--leaf); }
  .event-venue {
    position: absolute; right: 33px; top: 1058px; text-align: right;
    font-family: "Open Sans", sans-serif; font-weight: 600; font-size: 34px;
    line-height: 52px; color: var(--paper); letter-spacing: 1px;
  }
</style>
</head>
<body>
<main class="flyer">
  <svg class="backdrop" width="848" height="1200" viewBox="0 0 848 1200" aria-hidden="true">
    <rect width="848" height="1200" fill="var(--night)"/>
    <polygon points="0,0 655,0 0,952" fill="var(--coral)"/>
    <polygon points="0,942 334,1200 0,1200" fill="var(--paper)"/>
  </svg>

  <div class="art art--notes-top" role="img" aria-label="Illustration of a treble clef and colourful music notes on a wavy staff"></div>

  <h1 class="headline headline--top">NEON</h1>
  <div class="headline headline--bottom">REWIND</div>

  <svg class="lettering" width="848" height="1200" viewBox="0 0 848 1200" role="img" aria-label="80’s Dance Party">
    <text x="75" y="622" font-family="Bungee, sans-serif" font-size="430" textLength="212" lengthAdjust="spacingAndGlyphs"
          fill="var(--gold)" stroke="var(--rose)" stroke-width="10" paint-order="stroke">8</text>
    <text x="334" y="622" font-family="Bungee, sans-serif" font-size="430" textLength="208" lengthAdjust="spacingAndGlyphs"
          fill="var(--leaf)" stroke="#2e6e34" stroke-width="6" paint-order="stroke">0</text>
    <path d="M640 282 C670 276 678 304 666 334 L612 420 C604 430 592 424 594 412 L618 306 C622 290 628 284 640 282 Z"
          fill="var(--gold)" stroke="var(--ink)" stroke-width="6"/>
    <text x="660" y="528" font-family="Bungee, sans-serif" font-size="214" textLength="104" lengthAdjust="spacingAndGlyphs"
          fill="var(--rose)" stroke="#2b3a8a" stroke-width="6" paint-order="stroke">S</text>
    <text x="231" y="801" font-family="'Rubik Dirt', sans-serif" font-size="140" textLength="410" lengthAdjust="spacingAndGlyphs"
          fill="var(--rose)">DANCE</text>
    <text x="363" y="933" font-family="'Rubik Dirt', sans-serif" font-size="140" textLength="391" lengthAdjust="spacingAndGlyphs"
          fill="var(--amber)">PARTY</text>
  </svg>

  <div class="art art--boombox" role="img" aria-label="Illustration of a colourful retro boombox"></div>

  <div class="art art--notes-bottom" role="img" aria-label="Illustration of music notes and sparkles on a pink wavy staff"></div>

  <p class="event-date">
    <span class="date-day">SATURDAY,</span>
    <span>JUNE 26,</span>
    <span>2021</span>
  </p>

  <p class="event-venue">Location:<br>Brackenford Village.</p>
</main>
</body>
</html>
```